Redesign Craft Brewing Recipe Website

Originally built with Bootstrap just to get the site going, I am seeking a complete redesign of the sites home page and recipe page. I am an experienced web developer with no graphic background, initially just looking for psd mocks.

I prefer styles that are clean and modern, and would prefer anything that is fun, engaging, and has an organic feel to it. I currently have a cartoon rabbit as a logo, but it needs some modification/tweaking, so any help in that area would be great as well.

Current site:
http://kettlefinch.hostgridapps.net/

Current launch page/logo:
http://www.kettlefinch.com/

I like the overall layout of the elements currently, but the design sucks.
Updates

The launch page is at the following URL

Reason: Still looking for a more modern design. Designs received so far are too similar to the original.

My site is content based and does not contain images or products. Your design should not consist of large images.

Reason: The website has very little images, so the designs need to be more text and content based. The header needs to be very small and should not contain an ad rotater.

Target Market(s)

Home brewers, Craft brewers, Microbreweries, Brewpubs

Requirements
Must have
• Web 2.0 Look and Feel, Fun, Hip, Focus on content
Should not have
• A large photo as a header

```html
<!DOCTYPE html>
<html lang="en">
<head>
<meta charset="utf-8">
<title>Kettlefinch – Craft Beer Recipes</title>
<link rel="stylesheet" href="https://fonts.googleapis.com/css2?family=Arimo:ital,wght@0,400;0,700;1,700&family=Oswald:wght@500&display=swap">
<style>
:root{
  --bar-brown:#3b1e0f;
  --wood-dark:#5a2e14;
  --orange:#e8771e;
  --orange-deep:#c9560e;
  --orange-light:#f6a64a;
  --cream:#ece6dc;
  --wood:#efd8b2;
  --wood-light:#f5e4c6;
  --text:#3a3a3a;
  --muted:#8a8a8a;
  --link:#c8703a;
  --cell:#e6e3df;
  --cell-border:#c9c5bf;
  --extract:#d23a12;
  --partial:#e8861a;
  --allgrain:#1b9ad6;
  --srm-red:#b8401c;
  --srm-teal:#1f9a8c;
  --srm-green:#79b21d;
  --srm-blue:#1a7fc9;
  --white:#ffffff;
}
*{box-sizing:border-box;margin:0;padding:0}
html,body{width:696px;height:1200px;overflow:hidden}
body{position:relative;font-family:"Arimo",Arial,sans-serif;color:var(--text);background:var(--wood)}

.top-bar{position:absolute;top:0;left:0;width:696px;height:16px;background:var(--bar-brown)}
.search{position:absolute;left:81px;top:1px;width:116px;height:14px;background:var(--white);border-radius:2px;font-size:7px;color:var(--muted);padding:3px 4px}
.search svg{position:absolute;right:4px;top:3px}
.main-nav{position:absolute;right:82px;top:3px;display:flex;gap:24px;font-size:8px;font-weight:400;color:var(--white)}
.main-nav span{white-space:nowrap}

.masthead{position:absolute;top:16px;left:0;width:696px;height:103px;
  background:radial-gradient(ellipse at 50% 70%,var(--orange-light) 0%,var(--orange) 45%,var(--orange-deep) 100%)}
.brand{position:absolute;left:208px;top:58px;width:280px;height:60px;display:flex;align-items:center;justify-content:center;gap:8px}
.brand-dot{width:22px;height:22px;border-radius:50%;background:var(--white)}
.brand-name{font-size:30px;font-weight:700;color:var(--white);letter-spacing:.5px;white-space:nowrap}

.tagline-bar{position:absolute;top:119px;left:0;width:696px;height:26px;background:var(--cream)}
.tagline{position:absolute;left:201px;top:8px;font-size:9px;color:#333;white-space:nowrap}
.share{position:absolute;left:508px;top:7px;display:flex;gap:3px}
.share span{font-size:6px;background:#eef0f5;border:1px solid #b9c2d6;color:#3b5998;padding:1px 3px}
.social-mini{position:absolute;left:583px;top:7px;display:flex;gap:6px}
.social-mini i{display:block;width:10px;height:11px;background:#9b9189;border-radius:2px}

.filter-bar{position:absolute;top:145px;left:0;width:696px;height:35px;background:var(--white);border-bottom:1px solid #ddd}
.filter{position:absolute;top:6px;height:20px;background:#dcd8d2;border-radius:2px;font-size:8px;color:#444;padding:6px 7px;white-space:nowrap}
.filter::after{content:"";position:absolute;right:7px;top:8px;border:4px solid transparent;border-top-color:#999}
.sort{position:absolute;left:522px;top:6px;width:90px;height:20px;border:1px solid #ddd;border-radius:2px;font-size:8px;padding:5px 6px;color:#444;white-space:nowrap}
.sort b{color:var(--orange-deep);font-weight:400}
.sort::after{content:"";position:absolute;right:6px;top:8px;border:3.5px solid transparent;border-top-color:var(--orange-deep)}

.wood-field{position:absolute;top:181px;left:0;width:696px;height:944px;
  background:linear-gradient(90deg,var(--wood-light),var(--wood) 30%,var(--wood-light) 60%,var(--wood))}

.recipes{position:absolute;top:195px;left:83px;display:grid;grid-template-columns:repeat(4,124px);column-gap:11px;row-gap:12px}
.recipe{position:relative;width:124px;height:211px;background:var(--white);box-shadow:0 1px 3px rgba(60,30,10,.35)}
.recipe-photo{position:absolute;left:6px;top:4px;width:112px;height:111px;background:linear-gradient(160deg,#3a1c0a,#b8621a 55%,#f0b04a)}
.recipe-photo.alt{background:linear-gradient(200deg,#5b7a1e,#d9a23a 50%,#8a3d10)}
.recipe-photo.dark{background:linear-gradient(180deg,#1e120a,#8c3c12 60%,#e08a2a)}
.recipe-title{position:absolute;left:6px;top:94px;width:112px;height:21px;background:rgba(0,0,0,.55);color:var(--white);font-size:7.5px;padding:6px 0 0 7px;white-space:nowrap}
.stats-social{position:absolute;left:6px;top:121px;display:flex;gap:3px}
.stat-icon{width:11px;text-align:center;font-size:6px;color:#777}
.stat-icon svg{display:block;margin:0 auto 1px}
.method{position:absolute;right:6px;top:119px;height:9px;font-size:6.5px;color:var(--white);padding:1px 4px 0 10px;white-space:nowrap;clip-path:polygon(6px 0,100% 0,100% 100%,6px 100%,0 50%)}
.method.extract{background:var(--extract)}
.method.partial{background:var(--partial)}
.method.allgrain{background:var(--allgrain)}
.style{position:absolute;right:6px;top:130px;width:58px;height:11px;background:#e9e9e9;font-size:6.5px;color:var(--muted);text-align:right;padding:2px 3px 0 0;white-space:nowrap}
.recipe-desc{position:absolute;left:7px;top:150px;width:112px;font-size:7px;line-height:10px;color:#444}
.recipe-author{position:absolute;left:7px;top:172px;font-size:7px;color:var(--muted);white-space:nowrap}
.recipe-author a{color:var(--link);text-decoration:none}
.specs{position:absolute;left:1px;top:187px;display:flex;gap:2px}
.spec{width:23px;height:22px;background:var(--cell);border:1px solid var(--cell-border);font-size:6.5px;text-align:center;line-height:9px;padding-top:2px;color:#444}
.spec.srm{color:var(--white);border-color:transparent}
.srm.red{background:var(--srm-red)}
.srm.teal{background:var(--srm-teal)}
.srm.green{background:var(--srm-green)}
.srm.blue{background:var(--srm-blue)}

.footer-band{position:absolute;top:1125px;left:0;width:696px;height:20px;background:var(--wood-dark);border-top:3px solid #7a3f1b}
.footer-brand{position:absolute;left:278px;top:1092px;width:140px;height:52px;display:flex;align-items:center;justify-content:center;gap:6px;background:var(--cream);border-radius:70px 70px 0 0}
.footer-brand .brand-dot{width:14px;height:14px;background:var(--orange-deep)}
.footer-brand .brand-name{font-size:17px;color:var(--orange-deep)}
.footer-mugs{position:absolute;left:526px;top:1082px;width:70px;height:60px;border-radius:6px;background:linear-gradient(180deg,#f4ead8 0%,#d98a2a 35%,#8a3b10 100%)}

.mailing{position:absolute;top:1145px;left:0;width:696px;height:55px;background:var(--cream)}
.mailing-box{position:absolute;left:84px;top:0;width:522px;height:29px;background:var(--white);
  display:flex;align-items:center;padding:0 5px 0 7px;white-space:nowrap}
.mailing-title{font-family:"Oswald",Arial,sans-serif;font-weight:500;font-size:12.5px;line-height:1;color:var(--orange-deep);margin-right:6px}
.mailing-text{font-size:7px;color:#333;margin-right:4px}
.email{position:relative;width:117px;height:15px;border:1px solid #ccc;border-radius:8px;font-size:6.5px;color:#666;padding:3px 9px;margin-right:3px}
.join{position:absolute;right:-1px;top:-1px;width:22px;height:15px;border-radius:8px;background:var(--orange-deep);color:var(--white);font-size:6px;font-weight:700;text-align:center;padding-top:4px}
.connect{font-size:7px;font-style:italic;font-weight:700;color:#333;margin-right:4px}
.connect-icons{display:flex;gap:3px;margin-left:auto}
.connect-icons i{display:block;width:14px;height:15px;border-radius:2px}
.copyright{position:absolute;top:1179px;left:0;width:696px;text-align:center;font-size:7.5px;color:var(--link)}
</style>
</head>
<body>
<svg width="0" height="0" style="position:absolute">
  <defs>
    <symbol id="i-heart" viewBox="0 0 10 10"><path d="M5 9 1 5a2.3 2.3 0 0 1 4-3 2.3 2.3 0 0 1 4 3z" fill="#9a9a9a"/></symbol>
    <symbol id="i-chat" viewBox="0 0 10 10"><rect x="0" y="1" width="6" height="5" fill="#9a9a9a"/><rect x="4" y="4" width="6" height="5" fill="#b5b5b5"/></symbol>
    <symbol id="i-star" viewBox="0 0 10 10"><path d="M5 0.5 6.3 3.6 9.6 3.8 7 6 7.9 9.3 5 7.5 2.1 9.3 3 6 .4 3.8 3.7 3.6z" fill="#9a9a9a"/></symbol>
  </defs>
</svg>

<header class="top-bar">
  <div class="search">Search
    <svg width="7" height="7" viewBox="0 0 7 7"><circle cx="3" cy="3" r="2.2" fill="none" stroke="#333" stroke-width="1"/><path d="M4.6 4.6 6.6 6.6" stroke="#333" stroke-width="1.2"/></svg>
  </div>
  <nav class="main-nav"><span>Recipes</span><span>About ▾</span><span>Login</span></nav>
</header>

<section class="masthead" role="img" aria-label="Orange sunburst header with wheat ornament">
  <div class="brand"><span class="brand-dot"></span><span class="brand-name">Kettlefinch</span></div>
</section>

<section class="tagline-bar">
  <p class="tagline">Kettlefinch is the easiest way to create and share craft beer recipes.</p>
  <div class="share"><span>Like</span><span>0</span><span>Send</span></div>
  <div class="social-mini"><i></i><i></i></div>
</section>

<section class="filter-bar">
  <div class="filter" style="left:81px;width:74px">Brewing</div>
  <div class="filter" style="left:160px;width:73px">Styles</div>
  <div class="filter" style="left:238px;width:74px">Match Maker</div>
  <div class="sort">Sort by <b>› Trending</b></div>
</section>

<div class="wood-field"></div>

<main class="recipes">
  <article class="recipe">
    <div class="recipe-photo alt" role="img" aria-label="Photo of beer being poured"></div>
    <div class="recipe-title">Oak Bastard Sweet Mead</div>
    <div class="stats-social"><div class="stat-icon"><svg width="9" height="9"><use href="#i-heart"/></svg>10</div><div class="stat-icon"><svg width="9" height="9"><use href="#i-chat"/></svg>7</div><div class="stat-icon"><svg width="9" height="9"><use href="#i-star"/></svg>0</div></div>
    <div class="method extract">Extract</div><div class="style">Belgian Tripel</div>
    <p class="recipe-desc">Lorem ipsum dolor sit amet, consectetur adipisicing elit.</p>
    <p class="recipe-author">Created by <a href="#">Daniel Mercer</a></p>
    <div class="specs"><div class="spec">2.24%<br>ABV</div><div class="spec">24<br>IBU</div><div class="spec">1.006<br>FG</div><div class="spec">1.022<br>OG</div><div class="spec srm red">4<br>SRM</div></div>
  </article>
  <article class="recipe">
    <div class="recipe-photo dark" role="img" aria-label="Photo of beer glasses beside a barrel"></div>
    <div class="recipe-title">Oak Bastard Sweet Mead</div>
    <div class="stats-social"><div class="stat-icon"><svg width="9" height="9"><use href="#i-heart"/></svg>8</div><div class="stat-icon"><svg width="9" height="9"><use href="#i-chat"/></svg>15</div><div class="stat-icon"><svg width="9" height="9"><use href="#i-star"/></svg>0</div></div>
    <div class="method partial">PartialMash</div><div class="style">Mild</div>
    <p class="recipe-desc">Lorem ipsum dolor sit amet, consectetur adipisicing elit.</p>
    <p class="recipe-author">Created by <a href="#">Daniel Mercer</a></p>
    <div class="specs"><div class="spec">2.24%<br>ABV</div><div class="spec">24<br>IBU</div><div class="spec">1.006<br>FG</div><div class="spec">1.022<br>OG</div><div class="spec srm teal">4<br>SRM</div></div>
  </article>
  <article class="recipe">
    <div class="recipe-photo dark" role="img" aria-label="Photo of amber beers on a bar"></div>
    <div class="recipe-title">Oak Bastard Sweet Mead</div>
    <div class="stats-social"><div class="stat-icon"><svg width="9" height="9"><use href="#i-heart"/></svg>6</div><div class="stat-icon"><svg width="9" height="9"><use href="#i-chat"/></svg>3</div><div class="stat-icon"><svg width="9" height="9"><use href="#i-star"/></svg>0</div></div>
    <div class="method allgrain">AllGrain</div><div class="style">Belgian Tripel</div>
    <p class="recipe-desc">Lorem ipsum dolor sit amet, consectetur adipisicing elit.</p>
    <p class="recipe-author">Created by <a href="#">Daniel Mercer</a></p>
    <div class="specs"><div class="spec">2.24%<br>ABV</div><div class="spec">24<br>IBU</div><div class="spec">1.006<br>FG</div><div class="spec">1.022<br>OG</div><div class="spec srm green">4<br>SRM</div></div>
  </article>
  <article class="recipe">
    <div class="recipe-photo" role="img" aria-label="Photo of a pint of beer"></div>
    <div class="recipe-title">Oak Bastard Sweet Mead</div>
    <div class="stats-social"><div class="stat-icon"><svg width="9" height="9"><use href="#i-heart"/></svg>2</div><div class="stat-icon"><svg width="9" height="9"><use href="#i-chat"/></svg>9</div><div class="stat-icon"><svg width="9" height="9"><use href="#i-star"/></svg>0</div></div>
    <div class="method extract">Extract</div><div class="style">Belgian Tripel</div>
    <p class="recipe-desc">Lorem ipsum dolor sit amet, consectetur adipisicing elit.</p>
    <p class="recipe-author">Created by <a href="#">Daniel Mercer</a></p>
    <div class="specs"><div class="spec">2.24%<br>ABV</div><div class="spec">24<br>IBU</div><div class="spec">1.006<br>FG</div><div class="spec">1.022<br>OG</div><div class="spec srm blue">4<br>SRM</div></div>
  </article>

  <article class="recipe">
    <div class="recipe-photo alt" role="img" aria-label="Photo of beers with a barrel and wheat"></div>
    <div class="recipe-title">Oak Bastard Sweet Mead</div>
    <div class="stats-social"><div class="stat-icon"><svg width="9" height="9"><use href="#i-heart"/></svg>5</div><div class="stat-icon"><svg width="9" height="9"><use href="#i-chat"/></svg>20</div><div class="stat-icon"><svg width="9" height="9"><use href="#i-star"/></svg>0</div></div>
    <div class="method allgrain">AllGrain</div><div class="style">Belgian Tripel</div>
    <p class="recipe-desc">Lorem ipsum dolor sit amet, consectetur adipisicing elit.</p>
    <p class="recipe-author">Created by <a href="#">Daniel Mercer</a></p>
    <div class="specs"><div class="spec">2.24%<br>ABV</div><div class="spec">24<br>IBU</div><div class="spec">1.006<br>FG</div><div class="spec">1.022<br>OG</div><div class="spec srm blue">4<br>SRM</div></div>
  </article>
  <article class="recipe">
    <div class="recipe-photo dark" role="img" aria-label="Photo of two beer glasses"></div>
    <div class="recipe-title">Oak Bastard Sweet Mead</div>
    <div class="stats-social"><div class="stat-icon"><svg width="9" height="9"><use href="#i-heart"/></svg>0</div><div class="stat-icon"><svg width="9" height="9"><use href="#i-chat"/></svg>6</div><div class="stat-icon"><svg width="9" height="9"><use href="#i-star"/></svg>0</div></div>
    <div class="method extract">Extract</div><div class="style">Munich Helles</div>
    <p class="recipe-desc">Lorem ipsum dolor sit amet, consectetur adipisicing elit.</p>
    <p class="recipe-author">Created by <a href="#">Daniel Mercer</a></p>
    <div class="specs"><div class="spec">2.24%<br>ABV</div><div class="spec">24<br>IBU</div><div class="spec">1.006<br>FG</div><div class="spec">1.022<br>OG</div><div class="spec srm red">4<br>SRM</div></div>
  </article>
  <article class="recipe">
    <div class="recipe-photo alt" role="img" aria-label="Photo of beer pouring into a glass"></div>
    <div class="recipe-title">Oak Bastard Sweet Mead</div>
    <div class="stats-social"><div class="stat-icon"><svg width="9" height="9"><use href="#i-heart"/></svg>3</div><div class="stat-icon"><svg width="9" height="9"><use href="#i-chat"/></svg>8</div><div class="stat-icon"><svg width="9" height="9"><use href="#i-star"/></svg>0</div></div>
    <div class="method partial">PartialMash</div><div class="style">Mild</div>
    <p class="recipe-desc">Lorem ipsum dolor sit amet, consectetur adipisicing elit.</p>
    <p class="recipe-author">Created by <a href="#">Daniel Mercer</a></p>
    <div class="specs"><div class="spec">2.24%<br>ABV</div><div class="spec">24<br>IBU</div><div class="spec">1.006<br>FG</div><div class="spec">1.022<br>OG</div><div class="spec srm teal">4<br>SRM</div></div>
  </article>
  <article class="recipe">
    <div class="recipe-photo" role="img" aria-label="Photo of two beer mugs"></div>
    <div class="recipe-title">Oak Bastard Sweet Mead</div>
    <div class="stats-social"><div class="stat-icon"><svg width="9" height="9"><use href="#i-heart"/></svg>2</div><div class="stat-icon"><svg width="9" height="9"><use href="#i-chat"/></svg>10</div><div class="stat-icon"><svg width="9" height="9"><use href="#i-star"/></svg>0</div></div>
    <div class="method allgrain">AllGrain</div><div class="style">Belgian Tripel</div>
    <p class="recipe-desc">Lorem ipsum dolor sit amet, consectetur adipisicing elit.</p>
    <p class="recipe-author">Created by <a href="#">Daniel Mercer</a></p>
    <div class="specs"><div class="spec">2.24%<br>ABV</div><div class="spec">24<br>IBU</div><div class="spec">1.006<br>FG</div><div class="spec">1.022<br>OG</div><div class="spec srm green">4<br>SRM</div></div>
  </article>

  <article class="recipe">
    <div class="recipe-photo dark" role="img" aria-label="Photo of a frothy pint"></div>
    <div class="recipe-title">Oak Bastard Sweet Mead</div>
    <div class="stats-social"><div class="stat-icon"><svg width="9" height="9"><use href="#i-heart"/></svg>6</div><div class="stat-icon"><svg width="9" height="9"><use href="#i-chat"/></svg>9</div><div class="stat-icon"><svg width="9" height="9"><use href="#i-star"/></svg>0</div></div>
    <div class="method partial">PartialMash</div><div class="style">Mild</div>
    <p class="recipe-desc">Lorem ipsum dolor sit amet, consectetur adipisicing elit.</p>
    <p class="recipe-author">Created by <a href="#">Daniel Mercer</a></p>
    <div class="specs"><div class="spec">2.24%<br>ABV</div><div class="spec">24<br>IBU</div><div class="spec">1.006<br>FG</div><div class="spec">1.022<br>OG</div><div class="spec srm teal">4<br>SRM</div></div>
  </article>
  <article class="recipe">
    <div class="recipe-photo" role="img" aria-label="Photo of a beer mug"></div>
    <div class="recipe-title">Oak Bastard Sweet Mead</div>
    <div class="stats-social"><div class="stat-icon"><svg width="9" height="9"><use href="#i-heart"/></svg>5</div><div class="stat-icon"><svg width="9" height="9"><use href="#i-chat"/></svg>7</div><div class="stat-icon"><svg width="9" height="9"><use href="#i-star"/></svg>0</div></div>
    <div class="method allgrain">AllGrain</div><div class="style">English Cider</div>
    <p class="recipe-desc">Lorem ipsum dolor sit amet, consectetur adipisicing elit.</p>
    <p class="recipe-author">Created by <a href="#">Daniel Mercer</a></p>
    <div class="specs"><div class="spec">2.24%<br>ABV</div><div class="spec">24<br>IBU</div><div class="spec">1.006<br>FG</div><div class="spec">1.022<br>OG</div><div class="spec srm blue">4<br>SRM</div></div>
  </article>
  <article class="recipe">
    <div class="recipe-photo dark" role="img" aria-label="Photo of amber beers on a bar"></div>
    <div class="recipe-title">Oak Bastard Sweet Mead</div>
    <div class="stats-social"><div class="stat-icon"><svg width="9" height="9"><use href="#i-heart"/></svg>4</div><div class="stat-icon"><svg width="9" height="9"><use href="#i-chat"/></svg>3</div><div class="stat-icon"><svg width="9" height="9"><use href="#i-star"/></svg>0</div></div>
    <div class="method extract">Extract</div><div class="style">Belgian Tripel</div>
    <p class="recipe-desc">Lorem ipsum dolor sit amet, consectetur adipisicing elit.</p>
    <p class="recipe-author">Created by <a href="#">Daniel Mercer</a></p>
    <div class="specs"><div class="spec">2.24%<br>ABV</div><div class="spec">24<br>IBU</div><div class="spec">1.006<br>FG</div><div class="spec">1.022<br>OG</div><div class="spec srm green">4<br>SRM</div></div>
  </article>
  <article class="recipe">
    <div class="recipe-photo dark" role="img" aria-label="Photo of beers at a bar"></div>
    <div class="recipe-title">Oak Bastard Sweet Mead</div>
    <div class="stats-social"><div class="stat-icon"><svg width="9" height="9"><use href="#i-heart"/></svg>3</div><div class="stat-icon"><svg width="9" height="9"><use href="#i-chat"/></svg>11</div><div class="stat-icon"><svg width="9" height="9"><use href="#i-star"/></svg>0</div></div>
    <div class="method extract">Extract</div><div class="style">Belgian Tripel</div>
    <p class="recipe-desc">Lorem ipsum dolor sit amet, consectetur adipisicing elit.</p>
    <p class="recipe-author">Created by <a href="#">Daniel Mercer</a></p>
    <div class="specs"><div class="spec">2.24%<br>ABV</div><div class="spec">24<br>IBU</div><div class="spec">1.006<br>FG</div><div class="spec">1.022<br>OG</div><div class="spec srm red">4<br>SRM</div></div>
  </article>

  <article class="recipe">
    <div class="recipe-photo alt" role="img" aria-label="Photo of assorted cocktail and beer glasses"></div>
    <div class="recipe-title">Oak Bastard Sweet Mead</div>
    <div class="stats-social"><div class="stat-icon"><svg width="9" height="9"><use href="#i-heart"/></svg>8</div><div class="stat-icon"><svg width="9" height="9"><use href="#i-chat"/></svg>14</div><div class="stat-icon"><svg width="9" height="9"><use href="#i-star"/></svg>0</div></div>
    <div class="method extract">Extract</div><div class="style">Mild</div>
    <p class="recipe-desc">Lorem ipsum dolor sit amet, consectetur adipisicing elit.</p>
    <p class="recipe-author">Created by <a href="#">Daniel Mercer</a></p>
    <div class="specs"><div class="spec">2.24%<br>ABV</div><div class="spec">24<br>IBU</div><div class="spec">1.006<br>FG</div><div class="spec">1.022<br>OG</div><div class="spec srm teal">4<br>SRM</div></div>
  </article>
  <article class="recipe">
    <div class="recipe-photo" role="img" aria-label="Photo of beer being poured"></div>
    <div class="recipe-title">Oak Bastard Sweet Mead</div>
    <div class="stats-social"><div class="stat-icon"><svg width="9" height="9"><use href="#i-heart"/></svg>7</div><div class="stat-icon"><svg width="9" height="9"><use href="#i-chat"/></svg>50</div><div class="stat-icon"><svg width="9" height="9"><use href="#i-star"/></svg>0</div></div>
    <div class="method extract">Extract</div><div class="style">Belgian Tripel</div>
    <p class="recipe-desc">Lorem ipsum dolor sit amet, consectetur adipisicing elit.</p>
    <p class="recipe-author">Created by <a href="#">Daniel Mercer</a></p>
    <div class="specs"><div class="spec">2.24%<br>ABV</div><div class="spec">24<br>IBU</div><div class="spec">1.006<br>FG</div><div class="spec">1.022<br>OG</div><div class="spec srm green">4<br>SRM</div></div>
  </article>
  <article class="recipe">
    <div class="recipe-photo alt" role="img" aria-label="Photo of beers with a barrel and wheat"></div>
    <div class="recipe-title">Oak Bastard Sweet Mead</div>
    <div class="stats-social"><div class="stat-icon"><svg width="9" height="9"><use href="#i-heart"/></svg>4</div><div class="stat-icon"><svg width="9" height="9"><use href="#i-chat"/></svg>20</div><div class="stat-icon"><svg width="9" height="9"><use href="#i-star"/></svg>0</div></div>
    <div class="method allgrain">AllGrain</div><div class="style">English Cider</div>
    <p class="recipe-desc">Lorem ipsum dolor sit amet, consectetur adipisicing elit.</p>
    <p class="recipe-author">Created by <a href="#">Daniel Mercer</a></p>
    <div class="specs"><div class="spec">2.24%<br>ABV</div><div class="spec">24<br>IBU</div><div class="spec">1.006<br>FG</div><div class="spec">1.022<br>OG</div><div class="spec srm blue">4<br>SRM</div></div>
  </article>
  <article class="recipe">
    <div class="recipe-photo dark" role="img" aria-label="Photo of three beer glasses"></div>
    <div class="recipe-title">Oak Bastard Sweet Mead</div>
    <div class="stats-social"><div class="stat-icon"><svg width="9" height="9"><use href="#i-heart"/></svg>2</div><div class="stat-icon"><svg width="9" height="9"><use href="#i-chat"/></svg>8</div><div class="stat-icon"><svg width="9" height="9"><use href="#i-star"/></svg>0</div></div>
    <div class="method partial">PartialMash</div><div class="style">Belgian Tripel</div>
    <p class="recipe-desc">Lorem ipsum dolor sit amet, consectetur adipisicing elit.</p>
    <p class="recipe-author">Created by <a href="#">Daniel Mercer</a></p>
    <div class="specs"><div class="spec">2.24%<br>ABV</div><div class="spec">24<br>IBU</div><div class="spec">1.006<br>FG</div><div class="spec">1.022<br>OG</div><div class="spec srm red">4<br>SRM</div></div>
  </article>
</main>

<footer>
  <div class="footer-band"></div>
  <div class="footer-brand"><span class="brand-dot"></span><span class="brand-name">Kettlefinch</span></div>
  <div class="footer-mugs" role="img" aria-label="Illustration of beer mugs and hops"></div>
  <section class="mailing">
    <div class="mailing-box">
      <h2 class="mailing-title">JOIN OUR MAILING LIST</h2>
      <p class="mailing-text">Sign up for our e-mail list to receive updates</p>
      <div class="email">Your e-mail address<span class="join">JOIN</span></div>
      <p class="connect">Connect with us on</p>
      <div class="connect-icons"><i style="background:#4fb3e3"></i><i style="background:#3b5b99"></i><i style="background:#1d7ab5"></i></div>
    </div>
  </section>
  <p class="copyright">Copyright © 2013 Kettlefinch. All rights reserved.</p>
</footer>
</body>
</html>
```